Web Site for Strategy and Technology Consulting Company

We are looking for a website design that engages potential customers to understand our services and contact us. In this contest, we are looking for a homepage design, but the winning designer will be favored for the design of some of the more complicated interior pages of the site. An additional contest (or contests) for these pages will be added soon.

PLATROM AND RESPONSIVE DESIGN
The site will be implemented in WordPress using the Elementor page builder.
We are looking for a design that will look good on phones are well as laptop browsers.

UPLOADED FILES INCLUDE:
1a A wireframe of the homepage we are looking for. The Uploaded PDF also includes a draft of the text proposed for the homepage. Designers are free to go beyond the wireframe, but all elements of the wireframe should be included.
1b A Word document with the draft text of the homepage.
2a-d The Norvalith logo. Two versions are included – a dark version which works well against a light background, and a light version which works well against a dark background.
3 The Norvalith color palette with HEX and RGB values. Designers are not limited to this palette, but colors should be complementary.
4 A draft of the homepage menu
5 Service sheets with information on the services we provide

MORE ABOUT NORVALITH
Norvalith is a consulting company focused on transforming businesses through software. Our tagline, “Transformation Delivered,” recognizes the gap business often have between business transformation and the software they end up with. By listening to our customers and understanding their vision and where they are, we help get our customers where they want to go.

We increase our capability by working with many consultants and partners, allowing us to provide our customers with the best people and the software that best suits them.

Industry/Entity Type

Consulting

Number of Pages Required

1 page

Font styles to use
Sans Serif

Requirements
Must have
• the content represented on the wireframe uploaded
Nice to have
• interactive features, such as roll-over icons that reveal additional information

```html
<!DOCTYPE html>
<html lang="en">
<head>
<meta charset="utf-8">
<title>Norvalith — Transformation Delivered</title>
<link href="https://fonts.googleapis.com/css2?family=Inter:wght@400;500;600;700;800&display=swap" rel="stylesheet">
<style>
:root{
  --navy:#1d365c;
  --blue:#22609a;
  --blue-dark:#1c4f80;
  --yellow:#dfbc1f;
  --ink:#111418;
  --text:#5a5f66;
  --pale:#edf3fa;
  --faded:#b9d3ec;
  --footer:#2b3344;
  --grey-band:#efefef;
  --white:#ffffff;
}
*{margin:0;padding:0;box-sizing:border-box}
html,body{width:1200px;height:2870px;overflow:hidden}
body{font-family:'Inter',sans-serif;color:var(--ink);background:var(--white);position:relative}
.abs{position:absolute}
.btn{position:absolute;background:var(--yellow);color:var(--ink);font-size:14px;font-weight:500;border-radius:5px;display:flex;align-items:center;justify-content:center}

/* hero */
.hero{position:absolute;left:0;top:0;width:1200px;height:675px;overflow:hidden;background:linear-gradient(120deg,#1a3358 0%,#24476f 45%,#1c3a62 100%)}
.hero-photo{position:absolute;inset:0;background:radial-gradient(ellipse at 60% 40%,rgba(70,120,170,.45),rgba(20,45,80,0) 60%)}
.hero-accent{position:absolute;inset:0}
.logo{position:absolute;display:flex;align-items:center;gap:8px;font-weight:500;color:var(--white)}
.logo .mark{width:12px;height:12px;border-radius:50%;background:var(--yellow)}
.nav{position:absolute;left:402px;top:32px;display:flex;gap:38px;color:var(--white);font-size:14px;font-weight:500}
.nav span::after{content:"";display:inline-block;width:6px;height:6px;border-right:1.6px solid #fff;border-bottom:1.6px solid #fff;transform:rotate(45deg);margin-left:8px;position:relative;top:-3px}
.contact-btn{left:1006px;top:22px;width:133px;height:38px;background:var(--white);color:var(--ink)}
.hero h1{position:absolute;left:61px;top:166px;font-size:50px;font-weight:800;color:var(--white);letter-spacing:.3px}
.hero h1 em{font-style:normal;color:var(--yellow)}
.hero-copy{position:absolute;left:61px;top:235px;width:630px;font-size:14.5px;line-height:22.5px;color:var(--white)}
.checks{position:absolute;left:59px;top:334px;width:560px;list-style:none;color:var(--white);font-size:14.5px;line-height:22.5px}
.checks li{position:relative;padding-left:30px;margin-bottom:9px}
.checks li::before{content:"";position:absolute;left:0;top:6px;width:12px;height:12px;background:var(--yellow);border-radius:2px}
.checks li::after{content:"";position:absolute;left:3px;top:7px;width:5px;height:7px;border-right:2px solid var(--navy);border-bottom:2px solid var(--navy);transform:rotate(45deg)}
.pager{position:absolute;left:1121px;top:297px;width:38px;color:var(--white);font-size:15px;text-align:center}
.pager .on{width:38px;height:38px;border:1.5px solid #fff;border-radius:50%;display:flex;align-items:center;justify-content:center}
.pager div{height:33px;line-height:33px}

/* services */
.section-title{position:absolute;font-size:40px;font-weight:800;color:var(--ink)}
.section-title em{font-style:normal;color:var(--blue)}
.lead{position:absolute;font-size:14px;line-height:22.5px;color:var(--text)}
.card{position:absolute;top:880px;width:204px;height:253px;border:1px solid #dfe5ec;border-radius:6px;background:var(--white);text-align:center;box-shadow:0 2px 8px rgba(0,0,0,.04)}
.card.active{background:var(--blue);border-color:var(--blue)}
.card .icon{width:80px;height:80px;border-radius:50%;background:var(--blue);margin:21px auto 0;display:flex;align-items:center;justify-content:center}
.card.active .icon{background:var(--white)}
.card h3{margin-top:16px;font-size:16.5px;line-height:24px;font-weight:600;color:var(--ink);height:50px;display:flex;align-items:center;justify-content:center}
.card.active h3,.card.active p{color:var(--white)}
.card p{margin:6px 18px 0;font-size:14px;line-height:22.5px;color:var(--text)}

/* people */
.people-band{position:absolute;left:0;top:1376px;width:1200px;height:537px;background:var(--pale)}
.people-photo{position:absolute;left:542px;top:1209px;width:502px;height:431px;background:linear-gradient(160deg,#e6e9ec 0%,#c9cfd6 45%,#8c9ab0 75%,#d8dde3 100%)}
.marquee{position:absolute;top:1497px;font-size:58px;font-weight:800;white-space:nowrap}
.marquee.faint{color:var(--faded)}
.marquee.main{color:var(--blue-dark)}
.ring-list{position:absolute;left:551px;top:1665px;width:560px;list-style:none;font-size:14px;line-height:22.5px;color:var(--text)}
.ring-list li{position:relative;padding-left:37px;margin-bottom:9px}
.ring-list li::before{content:"";position:absolute;left:0;top:3px;width:16px;height:16px;border:2px solid var(--blue);border-radius:50%;border-right-color:transparent}

/* testimonials */
.eyebrow{position:absolute;left:0;width:1200px;top:1969px;text-align:center;font-size:14px;color:var(--text)}
.quote{position:absolute;top:2115px;width:340px;height:236px;background:var(--white);border:1px solid #e3e8ee;border-radius:6px;text-align:center;box-shadow:0 3px 10px rgba(0,0,0,.05)}
.quote.active{background:var(--blue);border-color:var(--blue)}
.quote::after{content:"";position:absolute;left:158px;bottom:-11px;width:20px;height:20px;background:inherit;transform:rotate(45deg);border-right:1px solid #e3e8ee;border-bottom:1px solid #e3e8ee}
.quote.active::after{border-color:var(--blue)}
.avatar{position:absolute;left:131px;top:-38px;width:78px;height:78px;border-radius:50%;background:linear-gradient(180deg,#cfd8e2,#8a7464);border:3px solid var(--white);box-shadow:0 0 0 2px var(--blue)}
.stars{margin-top:55px;color:var(--yellow);font-size:17px;letter-spacing:2px}
.quote p{margin:6px 34px 0;font-size:14px;line-height:22.5px;color:var(--text)}
.quote.active p{color:var(--white)}
.quote h4{margin-top:9px;font-size:16px;font-weight:700;color:var(--blue)}
.quote.active h4{color:var(--yellow)}
.quote small{display:block;font-size:12px;font-weight:500;color:var(--ink);margin-top:3px}
.quote.active small{color:var(--white)}
.arrow{position:absolute;top:2208px;width:41px;height:41px;border-radius:50%;display:flex;align-items:center;justify-content:center}

/* partners */
.partner-grey{position:absolute;left:0;top:2473px;width:1200px;height:89px;background:var(--grey-band)}
.partner-tag{position:absolute;left:61px;top:2478px;font-size:21px;line-height:28px;font-weight:700;color:var(--white)}
.partners{position:absolute;left:420px;top:2473px;width:720px;height:89px;display:flex;align-items:center;justify-content:space-between}
.partner{display:flex;align-items:center;gap:8px;font-size:27px;font-weight:500;color:#3c4350}
.partner i{width:20px;height:20px;border-radius:50%;background:var(--yellow)}

/* footer */
.footer{position:absolute;left:0;top:2562px;width:1200px;height:308px;background:var(--footer);color:#e8ebf0}
.footer h5{position:absolute;top:63px;font-size:16px;font-weight:600;color:var(--yellow)}
.footer .col{position:absolute;font-size:13px;line-height:20px}
.links div{height:31px}
.contact-row{position:relative;padding-left:30px;margin-bottom:10px}
.contact-row svg{position:absolute;left:0;top:2px}
.socials{position:absolute;left:888px;top:107px;display:flex;gap:5px}
.socials span{width:36px;height:36px;border-radius:50%;border:1.5px solid #d8dce3}
.socials span.on{background:var(--yellow);border-color:var(--yellow)}
.copyright{position:absolute;left:0;top:2833px;width:1200px;height:37px;border-top:1px solid #3e4658;text-align:center;font-size:12px;line-height:36px;color:#e8ebf0}
</style>
</head>
<body>

<header class="hero">
  <div class="hero-photo" role="img" aria-label="Laptop showing analytics dashboards in a blue-tinted workspace"></div>
  <svg class="hero-accent" width="1200" height="675" viewBox="0 0 1200 675">
    <defs><linearGradient id="gold" x1="0" y1="0" x2="0" y2="1"><stop offset="0" stop-color="#e2c236"/><stop offset="1" stop-color="#c8a51a"/></linearGradient></defs>
    <polygon points="934,0 1200,0 1200,675 735,675" fill="url(#gold)"/>
  </svg>
  <div class="logo" style="left:61px;top:14px;font-size:50px"><span class="mark"></span>Norvalith</div>
  <nav class="nav"><span>About Us</span><span>Services</span><span>Insights</span><span>Join Us</span></nav>
  <div class="btn contact-btn">Contact Us</div>
  <h1>Transformation <em>Delivered.</em></h1>
  <p class="hero-copy">We do more for our customers than implement software. We listen. We work to understand where they are in their transformation journey and where they want to go. We partner with them to clear the roadblocks that stand in their way, ensuring they reach their destination. At Norvalith, we:</p>
  <ul class="checks">
    <li>Focus on business value, with an emphasis on delivering value quickly.</li>
    <li>Meet our customers where they are without backing them up to the beginning of their journey.</li>
    <li>Provide a wide range of services, from strategy to product support.</li>
    <li>Commit to our customer’s long-term success.</li>
  </ul>
  <div class="btn" style="left:60px;top:504px;width:133px;height:37px">Our Story</div>
  <div class="pager"><div class="on">1</div><div style="margin-top:6px">2</div><div>3</div></div>
</header>

<h2 class="section-title" style="left:61px;top:742px">Transformation <em>Supported by Technology</em></h2>
<p class="lead" style="left:61px;top:794px;width:760px">During our early years, Norvalith focused only on business transformation. We came to realize that successful transformation often depended on quality software implementations, and often more than one. Now we focus on five things, the five things most businesses need to reach their goals.</p>
<div class="btn" style="left:984px;top:775px;width:155px;height:37px">How We Work</div>

<div class="card" style="left:60px"><div class="icon"><svg width="44" height="40" viewBox="0 0 44 40" fill="none" stroke="#fff" stroke-width="2"><rect x="3" y="4" width="34" height="24" rx="2"/><path d="M10 22v-5M16 22v-9M22 22v-7"/><circle cx="32" cy="22" r="6"/><path d="M36 26l6 6"/></svg></div><h3>Business<br>Transformation</h3><p>Define and execute your strategy.</p></div>
<div class="card active" style="left:280px"><div class="icon"><svg width="44" height="40" viewBox="0 0 44 40" fill="none" stroke="#1c4f80" stroke-width="2"><rect x="6" y="10" width="32" height="20" rx="2"/><path d="M18 36h8M22 30v6M12 25v-4M18 25v-7M24 25v-5M30 25v-9"/><circle cx="10" cy="6" r="4"/></svg></div><h3>ERP<br>Implementations</h3><p>Define and execute your strategy.</p></div>
<div class="card" style="left:500px"><div class="icon"><svg width="44" height="40" viewBox="0 0 44 40" fill="none" stroke="#fff" stroke-width="2"><rect x="4" y="10" width="36" height="26" rx="2"/><rect x="24" y="2" width="16" height="9" rx="2"/><circle cx="14" cy="23" r="5"/><path d="M24 19h12M24 25h12M24 31h8"/></svg></div><h3>CRM<br>Implementations</h3><p>Take your relationships to the next level.</p></div>
<div class="card" style="left:720px"><div class="icon"><svg width="44" height="40" viewBox="0 0 44 40" fill="none" stroke="#fff" stroke-width="2"><rect x="4" y="4" width="32" height="24" rx="2"/><path d="M10 22v-4M16 22v-8M22 22v-6"/><circle cx="30" cy="26" r="6"/><path d="M34 30l6 6"/></svg></div><h3>BI and Data</h3><p>Discover, connect, and trust your data.</p></div>
<div class="card" style="left:940px"><div class="icon"><svg width="44" height="44" viewBox="0 0 44 44" fill="none" stroke="#fff" stroke-width="2"><circle cx="22" cy="22" r="8"/><circle cx="22" cy="5" r="3"/><circle cx="22" cy="39" r="3"/><circle cx="5" cy="22" r="3"/><circle cx="39" cy="22" r="3"/><path d="M22 8v6M22 30v6M8 22h6M30 22h6"/></svg></div><h3>Building the Right<br>Team of People</h3><p>Hire resources for your transformation journey.</p></div>

<div class="people-band"></div>
<div class="people-photo" role="img" aria-label="Three colleagues smiling together around a laptop in a bright office"></div>
<div class="marquee faint" style="left:10px">People</div>
<div class="marquee main" style="left:409px">It’s the People</div>
<div class="marquee faint" style="left:1075px">It’s th</div>
<p class="lead" style="left:61px;top:1663px;width:425px">The world has changed in the past twenty years. The people you need might not all work for one company. Our clients want the best resources, available quickly. That’s why, in addition to our team of experts, we partner with:</p>
<ul class="ring-list">
  <li>A large network of expert consultants who are the best at what they do,</li>
  <li>Service providers all over the world to provide the resources and value that are right for you, available 24 x 7.</li>
</ul>
<p class="lead" style="left:551px;top:1754px;width:590px">People are invariably at the center of our customer’s success. Find out how we can add our experts to yours.</p>
<div class="btn" style="left:551px;top:1824px;width:160px;height:37px">Meet Our Team</div>

<div class="eyebrow">Testimonials</div>
<h2 class="section-title" style="left:0;width:1200px;text-align:center;top:1996px">What Our <em>Client Are Says...</em></h2>

<div class="arrow" style="left:54px;background:var(--blue)"><svg width="18" height="14" viewBox="0 0 18 14" fill="none" stroke="#fff" stroke-width="2"><path d="M17 7H2M7 1L1 7l6 6"/></svg></div>
<div class="quote" style="left:76px"><div class="avatar" role="img" aria-label="Client portrait"></div><div class="stars">★★★★★</div><p>Lorem Ipsum is simply dummy text of the printing and typesetting industry. Lorem Ipsum has been the industry’s standard dummy text.</p><h4>Marco Reyes</h4><small>Company Name</small></div>
<div class="quote active" style="left:430px"><div class="avatar" role="img" aria-label="Client portrait"></div><div class="stars">★★★★★</div><p>Lorem Ipsum is simply dummy text of the printing and typesetting industry. Lorem Ipsum has been the industry’s standard dummy text.</p><h4>Marco Reyes</h4><small>Company Name</small></div>
<div class="quote" style="left:783px"><div class="avatar" role="img" aria-label="Client portrait"></div><div class="stars">★★★★★</div><p>Lorem Ipsum is simply dummy text of the printing and typesetting industry. Lorem Ipsum has been the industry’s standard dummy text.</p><h4>Marco Reyes</h4><small>Company Name</small></div>
<div class="arrow" style="left:1102px;background:var(--yellow)"><svg width="18" height="14" viewBox="0 0 18 14" fill="none" stroke="#111" stroke-width="2"><path d="M1 7h15M11 1l6 6-6 6"/></svg></div>

<div class="partner-grey"></div>
<svg class="abs" style="left:0;top:2451px" width="400" height="111" viewBox="0 0 400 111"><polygon points="0,0 399,0 331,111 0,111" fill="#22609a"/></svg>
<div class="partner-tag">Transformation Supported<br>by Technology</div>
<div class="partners">
  <div class="partner"><i></i>Lumora</div>
  <div class="partner"><i></i>Brintel</div>
  <div class="partner"><i></i>Avenor</div>
  <div class="partner"><i></i>Ideon</div>
  <div class="partner"><i></i>Hexlo</div>
</div>

<footer class="footer">
  <div class="logo" style="left:61px;top:40px;font-size:46px"><span class="mark"></span>Norvalith</div>
  <p class="col" style="left:61px;top:107px;width:240px">Lorem Ipsum is simply dummy text of the printing and typesetting industry. Lorem Ipsum has been the industry’s.</p>
  <h5 style="left:339px">Quick Links:</h5>
  <div class="col links" style="left:339px;top:98px"><div>About Us</div><div>Services</div><div>Insights</div><div>Join Us</div><div>Contact Us</div></div>
  <h5 style="left:614px">Contact Us:</h5>
  <div class="col" style="left:612px;top:95px;width:250px">
    <div class="contact-row"><svg width="16" height="18" viewBox="0 0 16 18"><path d="M8 1a5 5 0 0 0-5 5c0 4 5 9 5 9s5-5 5-9a5 5 0 0 0-5-5z" fill="#dfbc1f"/><circle cx="8" cy="6" r="2" fill="#2b3344"/></svg>123, Lorem Ipsum is simply dummy text of the printing.</div>
    <div class="contact-row" style="font-weight:600"><svg width="16" height="16" viewBox="0 0 16 16"><path d="M3 1l3 3-2 2c1 3 3 5 6 6l2-2 3 3-2 2C7 15 1 9 1 3z" fill="#dfbc1f"/></svg>555 014 2290</div>
    <div class="contact-row"><svg width="18" height="14" viewBox="0 0 18 14"><rect x="1" y="2" width="16" height="11" fill="#dfbc1f"/><path d="M1 2l8 6 8-6" stroke="#2b3344" stroke-width="1.5" fill="none"/></svg>info@norvalith.com</div>
  </div>
  <h5 style="left:890px">Connect With Us:</h5>
  <div class="socials"><span></span><span></span><span class="on"></span><span></span></div>
</footer>
<div class="copyright" style="background:var(--footer)">© 2023 Copyright. Norvalith. All Right Reserved.</div>

</body>
</html>
```